Custom Anatomical Healing Abutment Flyer

Need a Flyer (4x6 inch) color printed suffer for orders..
See attachment for what I'm looking for. just need it to look Nice (eye candy)...

- reduce the number of steps to 5 (pictures included)

you can remove the watermark (have approval from him to use this) just need to add "permission from lorvantic"

- Tag Line: (can change the wording if needed)
Custom Anatomical Healing Abutment
Available in Silicone and 3D printed

Target Market(s)

Letting customers know of new product available.

Font styles to use
Sans Serif

Colors

Designer to choose colors to be used in the design.

Requirements
Must have
• - reduce the number of steps to 5 (pictures included)
• you can remove the watermark (have approval from him to use this) just need to add "permission from lorvantic"
Nice to have
• - Tag Line: (can change the wording if needed)
• Custom Anatomical Healing Abutment
• Available in Silicone and 3D printed

```html
<!DOCTYPE html>
<html lang="en">
<head>
<meta charset="utf-8">
<title>Custom Anatomical Healing Abutment Flyer</title>
<link rel="stylesheet" href="https://fonts.googleapis.com/css2?family=Oswald:wght@500;700&family=Questrial&display=swap">
<style>
  :root {
    --navy: #1c3f8f;
    --navy-dark: #0f2a66;
    --ink: #1e1e1e;
    --grey: #3a3a3a;
    --paper-light: #fbfbfb;
    --paper-dark: #d6d6d6;
    --green: #1fa34a;
    --orange: #f39c12;
    --yellow: #f2c500;
    --lime: #8cc63f;
    --teal: #1aa6b7;
  }
  html, body {
    margin: 0;
    padding: 0;
    width: 707px;
    height: 1200px;
    overflow: hidden;
  }
  .flyer {
    position: relative;
    width: 707px;
    height: 1200px;
    background: radial-gradient(ellipse at 50% 40%, var(--paper-light) 0%, #eeeeee 55%, var(--paper-dark) 100%);
    font-family: "Oswald", sans-serif;
    text-align: center;
  }
  .headline {
    position: absolute;
    top: 44px;
    left: 0;
    width: 100%;
    margin: 0;
  }
  .headline-main {
    display: block;
    font-weight: 700;
    font-size: 66px;
    line-height: 1;
    color: var(--navy);
    letter-spacing: 0.5px;
  }
  .headline-sub {
    display: block;
    margin-top: 12px;
    font-family: "Questrial", sans-serif;
    font-weight: 400;
    font-size: 38px;
    line-height: 1;
    letter-spacing: 11px;
    padding-left: 11px;
    color: var(--grey);
  }
  .steps {
    position: absolute;
    left: 0;
    top: 0;
  }
  .step-number {
    font-family: "Oswald", sans-serif;
    font-weight: 500;
    font-size: 24px;
    fill: var(--ink);
  }
  .availability {
    position: absolute;
    top: 990px;
    left: 0;
    width: 100%;
    margin: 0;
  }
  .availability-line {
    display: block;
    font-weight: 700;
    font-size: 38px;
    line-height: 1.1;
    color: var(--ink);
  }
  .availability-accent {
    display: block;
    font-weight: 700;
    font-size: 88px;
    line-height: 1.05;
    letter-spacing: 2px;
    background: linear-gradient(180deg, #8cbcf0 0%, #2a62c4 45%, var(--navy-dark) 100%);
    -webkit-background-clip: text;
    background-clip: text;
    color: transparent;
  }
  .permission {
    position: absolute;
    top: 1150px;
    left: 0;
    width: 100%;
    margin: 0;
    display: flex;
    justify-content: center;
    align-items: center;
    gap: 10px;
    font-family: "Questrial", sans-serif;
    font-size: 13px;
    letter-spacing: 0.5px;
    color: var(--navy);
    text-transform: uppercase;
  }
  .permission::before,
  .permission::after {
    content: "";
    width: 70px;
    height: 1.5px;
    background: var(--navy);
  }
</style>
</head>
<body>
<main class="flyer">
  <h1 class="headline">
    <span class="headline-main">CUSTOM ANATOMICAL</span>
    <span class="headline-sub">HEALING ABUTMENT</span>
  </h1>

  <svg class="steps" width="707" height="1200" viewBox="0 0 707 1200" aria-label="Five step process around patients">
    <defs>
      <radialGradient id="center-photo" cx="50%" cy="45%" r="65%">
        <stop offset="0%" stop-color="#f3dcc8"/>
        <stop offset="55%" stop-color="#d9b79c"/>
        <stop offset="100%" stop-color="#a8cbc4"/>
      </radialGradient>
      <radialGradient id="photo-tray" cx="50%" cy="60%" r="70%">
        <stop offset="0%" stop-color="#5b6a78"/>
        <stop offset="100%" stop-color="#151c24"/>
      </radialGradient>
      <radialGradient id="photo-glove" cx="45%" cy="45%" r="70%">
        <stop offset="0%" stop-color="#5f7f88"/>
        <stop offset="100%" stop-color="#6fc2b8"/>
      </radialGradient>
      <radialGradient id="photo-light" cx="45%" cy="40%" r="70%">
        <stop offset="0%" stop-color="#5a4cc8"/>
        <stop offset="55%" stop-color="#1d2b45"/>
        <stop offset="100%" stop-color="#6cc4b6"/>
      </radialGradient>
      <radialGradient id="photo-mouth" cx="50%" cy="50%" r="70%">
        <stop offset="0%" stop-color="#e4d6cc"/>
        <stop offset="60%" stop-color="#b4606c"/>
        <stop offset="100%" stop-color="#7a2d3a"/>
      </radialGradient>
      <radialGradient id="photo-gum" cx="50%" cy="45%" r="70%">
        <stop offset="0%" stop-color="#e05a6e"/>
        <stop offset="60%" stop-color="#c96a78"/>
        <stop offset="100%" stop-color="#eadbd4"/>
      </radialGradient>
      <filter id="soft-shadow" x="-20%" y="-20%" width="140%" height="140%">
        <feDropShadow dx="0" dy="3" stdDeviation="5" flood-color="#000" flood-opacity="0.22"/>
      </filter>
    </defs>

    <g class="step-bridges" stroke-width="66" stroke-linecap="round" fill="none" filter="url(#soft-shadow)">
      <path d="M353 360 Q 480 500 568 540" stroke="var(--orange)"/>
      <path d="M568 540 Q 470 690 485 835" stroke="var(--yellow)"/>
      <path d="M485 835 Q 353 760 221 835" stroke="var(--lime)"/>
      <path d="M221 835 Q 236 690 138 560" stroke="var(--teal)"/>
      <path d="M138 560 Q 226 500 353 360" stroke="var(--green)"/>
    </g>

    <g class="center-portrait">
      <circle cx="353" cy="630" r="134" fill="#ffffff"/>
      <circle cx="353" cy="630" r="122" fill="url(#center-photo)" role="img" aria-label="Photo of a smiling couple"/>
    </g>

    <g class="step step-1">
      <circle cx="353" cy="360" r="100" fill="var(--green)" stroke="#ffffff" stroke-width="6"/>
      <circle cx="353" cy="360" r="82" fill="url(#photo-tray)" role="img" aria-label="Step 1 photo: handpiece milling an abutment in a dark tray"/>
    </g>
    <g class="step step-2">
      <circle cx="568" cy="540" r="100" fill="var(--orange)" stroke="#ffffff" stroke-width="6"/>
      <circle cx="568" cy="540" r="82" fill="url(#photo-glove)" role="img" aria-label="Step 2 photo: gloved hand placing silicone into a tray"/>
    </g>
    <g class="step step-3">
      <circle cx="485" cy="835" r="100" fill="var(--yellow)" stroke="#ffffff" stroke-width="6"/>
      <circle cx="485" cy="835" r="82" fill="url(#photo-light)" role="img" aria-label="Step 3 photo: curing light over the abutment mould"/>
    </g>
    <g class="step step-4">
      <circle cx="221" cy="835" r="100" fill="var(--lime)" stroke="#ffffff" stroke-width="6"/>
      <circle cx="221" cy="835" r="82" fill="url(#photo-mouth)" role="img" aria-label="Step 4 photo: healing abutment seated between teeth"/>
    </g>
    <g class="step step-5">
      <circle cx="138" cy="560" r="100" fill="var(--teal)" stroke="#ffffff" stroke-width="6"/>
      <circle cx="138" cy="560" r="82" fill="url(#photo-gum)" role="img" aria-label="Step 5 photo: healed gum contour around implant"/>
    </g>

    <g class="step-badges">
      <circle cx="277" cy="418" r="17" fill="#fff"/>
      <text class="step-number" x="277" y="427" text-anchor="middle">1</text>
      <circle cx="503" cy="471" r="17" fill="#fff"/>
      <text class="step-number" x="503" y="480" text-anchor="middle">2</text>
      <circle cx="512" cy="740" r="17" fill="#fff"/>
      <text class="step-number" x="512" y="749" text-anchor="middle">3</text>
      <circle cx="292" cy="834" r="17" fill="#fff"/>
      <text class="step-number" x="292" y="843" text-anchor="middle">4</text>
      <circle cx="166" cy="637" r="17" fill="#fff"/>
      <text class="step-number" x="166" y="646" text-anchor="middle">5</text>
    </g>
  </svg>

  <h2 class="availability">
    <span class="availability-line">AVAILABLE IN SILICONE AND</span>
    <span class="availability-accent">3D PRINTED</span>
  </h2>

  <p class="permission">Permission from lorvantic</p>
</main>
</body>
</html>
```